Deck Construction Company Billboard Design needed

We are a deck company with a 10'x32' billboard to fill with an advertisement. I'd like this ad to be 75% photo, 25% color-filled background with white text over (space to be divided side-to-side with line of some sort). This billboard artwork must be clearly legible and simple. The information I need on the billboard is as follows:
Plank QR (company name)
plankqr.ca
Outdoor Living Spaces
416-283-9061
Attached is a copy of the logo and photos I'd like to use (please choose one photo per billboard design)

Target Market(s)

30-70 year old home owners

Industry/Entity Type

Deck Builder

Font styles to use
Other font styles liked:
• Calibri

Colors
0054AA
0677BA
7BADD7
CADEEF
E8F1F8

Requirements
Must have
• Clear, simple white text. Dark blue fill, red accent
Nice to have
• Layering of photo and text
Should not have
• Too much to read

```html
<!DOCTYPE html>
<html lang="en">
<head>
<meta charset="utf-8">
<title>Plank QR – Outdoor Living Spaces Billboard</title>
<link href="https://fonts.googleapis.com/css2?family=Figtree:wght@600;700;800&display=swap" rel="stylesheet">
<style>
  :root {
    --navy: #0f2844;
    --red: #e31e25;
    --red-light: #ea4a55;
    --white: #ffffff;
    --stage: #eef2f6;
    --photo-pool: #2f5d96;
    --photo-deck: #8e959e;
  }
  html, body {
    margin: 0;
    width: 1200px;
    height: 898px;
    overflow: hidden;
    background: var(--stage);
  }
  .billboard {
    position: absolute;
    left: 40px;
    top: 270px;
    width: 1120px;
    height: 358px;
    display: block;
    box-shadow: 0 6px 18px rgba(15, 40, 68, 0.25);
  }
  .billboard text {
    font-family: "Figtree", "Calibri", sans-serif;
  }
  .web-address { fill: var(--navy); font-weight: 700; font-size: 62px; }
  .phone-number { fill: var(--white); font-weight: 700; font-size: 106px; }
  .brand-name { fill: var(--white); font-weight: 800; font-size: 90px; letter-spacing: 2px; }
  .tagline { fill: var(--white); font-weight: 800; font-size: 96px; }
  .fill-navy { fill: var(--navy); }
  .fill-red { fill: var(--red); }
  .fill-red-light { fill: var(--red-light); }
  .fill-white { fill: var(--white); }
</style>
</head>
<body>
<svg class="billboard" viewBox="0 0 1644 526" xmlns="http://www.w3.org/2000/svg">
  <defs>
    <linearGradient id="photoTones" x1="0" y1="0.3" x2="1" y2="0.7">
      <stop offset="0.15" stop-color="var(--photo-pool)"/>
      <stop offset="0.75" stop-color="var(--photo-deck)"/>
    </linearGradient>
    <linearGradient id="steelStrip" x1="0" y1="0" x2="1" y2="0">
      <stop offset="0" stop-color="#ffffff" stop-opacity="0"/>
      <stop offset="0.35" stop-color="#6a7686"/>
      <stop offset="1" stop-color="#e4e8ee"/>
    </linearGradient>
  </defs>

  <rect class="deck-photo" x="0" y="0" width="1644" height="526" fill="url(#photoTones)"
        role="img" aria-label="Aerial photo of a grey composite deck around a blue swimming pool with lounge chairs and trees"/>

  <!-- left accent stripes -->
  <polygon class="fill-red" points="0,80 90,80 0,235"/>
  <polygon class="fill-navy" points="90,80 170,80 0,370 0,235"/>

  <!-- web address tab -->
  <polygon class="fill-red" points="395,0 732,0 708,30 378,30"/>
  <polygon class="fill-white" points="0,0 420,0 372,80 0,80"/>
  <text class="web-address" x="30" y="62">plankqr.ca</text>

  <!-- brand panel -->
  <polygon class="fill-navy" points="1165,0 1644,0 1644,110 1575,230 1035,230"/>
  <polygon class="fill-white" points="1575,230 1644,110 1644,230"/>
  <polygon points="1085,204 1532,204 1517,230 1068,230" fill="url(#steelStrip)"/>
  <text class="brand-name" x="1610" y="133" text-anchor="end">PLANK QR</text>

  <!-- tagline panel -->
  <path class="fill-red" d="M810,526 L990,272 Q1018,232 1065,230 L1644,230 L1644,526 Z"/>
  <polygon class="fill-red-light" points="1352,526 1522,230 1644,230 1644,526"/>
  <text class="tagline" text-anchor="middle">
    <tspan x="1319" y="324">OUTDOOR</tspan>
    <tspan x="1319" y="407">LIVING</tspan>
    <tspan x="1319" y="491">SPACES</tspan>
  </text>

  <!-- phone band -->
  <polygon class="fill-red" points="0,460 795,460 752,526 0,526"/>
  <text class="phone-number" x="50" y="505">416-283-9061</text>
</svg>
</body>
</html>
```